Paddock Guard Solutions Business Cards and Logo

I am commencing a niche safety business for horse racing stables and breeders. The registered business name is 'Paddock Guard Solutions'. It is a business of TOVEN Advisory. The page on my website www.tovenadvisory.com.au outlines the services offered.

The most important aspect is the development of a simple logo. I envisage a logo something like three horse heads in a simple outline to form the letter E for Paddock Guard Solutions. Alternatively a simple line drawing of a horse head that might be used on stationery and merchandise for example, a logo that might be used on a polo shirt and bumber stickers.

Industry/Entity Type

Business

Contact Information for Business Card

Martin Keble
Director
Paddock Guard Solutions
'Good stables are safe stables'
A business of TOVEN Advisory
0491 738 205
martin@tovenadvisory.com.au
www.tovenadvisory.com.au

Requirements
Must have
• Logo (see above)
Name: Martin Keble
Title: Director
Business Name: Paddock Guard Solutions
Motto: 'Good stables are safe stables'
A business of TOVEN Advisory (smaller print and probably ilalicised)
Phone: 0491 738 205
Email: martin@tovenadvisory.com.au
Web Address: www.tovenadvisory.com.au

```html
<!DOCTYPE html>
<html lang="en">
<head>
<meta charset="utf-8">
<title>Paddock Guard Solutions – Business Card</title>
<link rel="stylesheet" href="https://fonts.googleapis.com/css2?family=Arimo:wght@400&family=Open+Sans:wght@400&family=Tinos:ital@0;1&display=swap">
<style>
  :root {
    --paper: #ffffff;
    --ink: #000000;
    --ink-soft: #4d4d4d;
    --label: #555555;
    --mark-text: #666666;
    --art-light: #e2e2e2;
    --art-mid: #b4b4b4;
    --art-dark: #8c8c8c;
  }
  html, body {
    margin: 0;
    padding: 0;
    overflow: hidden;
    background: var(--paper);
  }
  .card {
    position: relative;
    width: 1200px;
    height: 741px;
    background: var(--paper);
    overflow: hidden;
  }
  .person {
    position: absolute;
    left: 51px;
    top: 62px;
    font-family: "Arimo", Arial, sans-serif;
  }
  .person-name {
    margin: 0;
    font-size: 58px;
    font-weight: 400;
    line-height: 1;
    color: var(--ink);
  }
  .person-title {
    margin: 8px 0 0 2px;
    font-size: 39px;
    line-height: 1;
    color: var(--ink-soft);
  }
  .contact {
    position: absolute;
    left: 605px;
    top: 68px;
    margin: 0;
    display: grid;
    grid-template-columns: 71px auto;
    row-gap: 6px;
    font-family: "Open Sans", Arial, sans-serif;
    font-size: 34px;
    line-height: 40px;
  }
  .contact dt {
    color: var(--label);
    font-weight: 400;
  }
  .contact dd {
    margin: 0;
    color: var(--ink);
  }
  .horse-art {
    position: absolute;
    left: 172px;
    top: 200px;
    width: 420px;
    height: 215px;
    border-radius: 6px;
    background: linear-gradient(100deg, var(--art-mid) 0%, var(--art-dark) 45%, var(--art-light) 100%);
  }
  .brand-mark {
    position: absolute;
    left: 352px;
    top: 440px;
    margin: 0;
    font-family: "Arimo", Arial, sans-serif;
    font-size: 60px;
    font-weight: 400;
    line-height: 1;
    color: var(--mark-text);
    white-space: nowrap;
  }
  .business {
    position: absolute;
    left: 51px;
    top: 600px;
  }
  .business-name {
    margin: 0;
    font-family: "Arimo", Arial, sans-serif;
    font-size: 47px;
    font-weight: 400;
    line-height: 1;
    color: var(--ink);
  }
  .business-parent {
    margin: 14px 0 0 0;
    font-family: "Tinos", "Times New Roman", serif;
    font-style: italic;
    font-size: 32px;
    line-height: 1;
    color: var(--ink-soft);
    white-space: nowrap;
  }
</style>
</head>
<body>
<main class="card">
  <header class="person">
    <h1 class="person-name">Martin Keble</h1>
    <p class="person-title">Director</p>
  </header>

  <dl class="contact">
    <dt>T</dt><dd>0491 738 205</dd>
    <dt>E</dt><dd>martin@tovenadvisory.com.au</dd>
    <dt>W</dt><dd>www.tovenadvisory.com.au</dd>
  </dl>

  <div class="horse-art" role="img" aria-label="Grey-toned horse head illustration with flowing mane"></div>

  <p class="brand-mark">Paddock Guard Solutions</p>

  <footer class="business">
    <p class="business-name">Paddock Guard Solutions</p>
    <p class="business-parent">'Good stables are safe stables' — A business of TOVEN Advisory</p>
  </footer>
</main>
</body>
</html>
```